Business cards and stationary for high end Chiropractic wellness center
Harborline Chiropractic Center
Professional
Dr. Tobias K. Feldmore
Board Certified Chiropractor
4382 Elmhaven Ave
Suite 100
Frederick, MD 21745
care@drfeldmore-example.com
www.harborlineclinic-example.com
Not sure we will have the email on the business cards as we do not like the Doc's personal email on his cards.
The Stationary will not have the Doctor's info only the clinic info
This should be blank
additional color layout

```html
<!DOCTYPE html>
<html lang="en">
<head>
<meta charset="utf-8">
<title>Harborline Chiropractic Center — Stationery Set</title>
<link rel="stylesheet" href="https://fonts.googleapis.com/css2?family=Montserrat:wght@600;700&family=Open+Sans:wght@400;600&display=swap">
<style>
  :root{
    --purple:#4b4586;
    --green:#8dc63f;
    --paper:#ffffff;
    --ground:#ebebed;
    --ink:#5a5a66;
    --muted:#9a9aa4;
  }
  *{box-sizing:border-box;margin:0;padding:0}
  html,body{width:1200px;height:936px;overflow:hidden;background:var(--ground)}
  body{position:relative;font-family:"Open Sans",Arial,sans-serif;color:var(--ink)}
  .sheet{position:absolute;background:var(--paper);box-shadow:0 2px 6px rgba(0,0,0,.18);overflow:hidden}

  /* footer band: flat purple block with a thin green rule above */
  .band{position:absolute;left:0;right:0;bottom:0;background:var(--purple)}
  .band::before{content:"";position:absolute;left:0;right:0;top:-6px;height:2px;background:var(--green)}
  .web{position:absolute;color:#fff;font-family:"Montserrat",Arial,sans-serif;font-weight:600;letter-spacing:.02em;white-space:nowrap}

  .brand{display:flex;align-items:center;gap:6px;font-family:"Montserrat",Arial,sans-serif;font-weight:700;color:var(--purple);line-height:1.1;text-transform:uppercase}
  .brand .dot{border-radius:50%;background:var(--purple);flex:none}

  /* letterhead */
  .letterhead{left:173px;top:63px;width:297px;height:559px}
  .letterhead .brand{position:absolute;left:12px;top:18px;font-size:9px;width:130px}
  .letterhead .brand .dot{width:16px;height:16px}
  .contact{position:absolute;right:14px;top:18px;font-size:5px;line-height:1.55;color:var(--muted)}
  .letter{position:absolute;left:18px;top:120px;width:250px;font-size:4.6px;line-height:1.6;color:var(--muted)}
  .letter p{margin-bottom:9px}
  .letter .sign{margin-top:20px;width:34px;border-bottom:1px solid var(--muted);height:10px;margin-bottom:6px}
  .letterhead .band{height:36px}
  .letterhead .web{right:14px;bottom:12px;font-size:7px}

  /* folder */
  .folder{left:507px;top:56px;width:627px;height:566px}
  .folder .brand{position:absolute;left:0;right:0;top:190px;flex-direction:column;gap:16px;font-size:31px;text-align:center}
  .folder .brand .dot{width:78px;height:78px}
  .folder .band{height:62px}
  .folder .band::before{top:-9px;height:3px}
  .folder .web{right:28px;bottom:21px;font-size:13px}

  /* business cards */
  .card-front{left:84px;top:665px;width:157px;height:76px}
  .card-front .brand{position:absolute;left:8px;top:8px;font-size:5.2px;width:70px;gap:4px}
  .card-front .brand .dot{width:9px;height:9px}
  .card-front .who{position:absolute;right:8px;top:8px;font-size:4.2px;line-height:1.5;text-align:right;color:var(--muted)}
  .card-front .who strong{color:var(--purple);font-weight:600;font-size:4.8px}
  .card-front .band{height:12px}
  .card-front .band::before{top:-4px;height:1px}
  .card-back{left:84px;top:761px;width:157px;height:86px}
  .card-back .brand{position:absolute;left:10px;top:16px;font-size:8px;width:110px;opacity:.18}
  .card-back .brand .dot{width:16px;height:16px}
  .card-back .tag{position:absolute;left:10px;bottom:9px;font-size:5px;color:var(--purple);font-weight:600}

  /* envelopes */
  .envelope{left:266px;top:665px;width:406px;height:185px}
  .envelope .brand{position:absolute;left:12px;top:12px;font-size:9px;width:140px}
  .envelope .brand .dot{width:16px;height:16px}
  .envelope .band{height:34px}
  .envelope .web{right:20px;bottom:11px;font-size:8px}
  .envelope-back{left:703px;top:665px;width:413px;height:185px}
  .envelope-back svg{position:absolute;inset:0}
  .envelope-back .web{left:0;right:0;top:16px;text-align:center;color:var(--purple);font-size:9px}
</style>
</head>
<body>

<section class="sheet letterhead">
  <div class="brand"><span class="dot"></span><span>Harborline Chiropractic Center</span></div>
  <div class="contact">
    4382 Elmhaven Ave, Suite 100<br>
    Frederick, MD 21745<br>
    (301) 555-0147<br>
    Fax (301) 555-0148<br>
    www.harborlineclinic-example.com
  </div>
  <div class="letter">
    <p>June 4, 2024</p>
    <p>Dear Patient,<br>4382 Elmhaven Ave, Frederick, MD 21745</p>
    <p>Thank you for choosing our clinic for your care. Our team is committed to helping you move freely, recover fully and feel your best every day. We look forward to supporting your goals with careful assessment, clear guidance and a treatment plan shaped around your needs.</p>
    <p>Each visit begins with a short review of your progress. We adjust, stretch and strengthen with gentle methods, and we explain every step so you always know what comes next. Please arrive a few minutes early and bring any recent notes from other providers.</p>
    <p>If you have questions before your next appointment, our front desk is happy to help. We value your trust and will keep working with you to build lasting comfort and strength.</p>
    <p>Kind Regards,</p>
    <div class="sign"></div>
    <p>Care Team<br>Clinic Director</p>
  </div>
  <div class="band"></div>
  <div class="web">www.harborlineclinic-example.com</div>
</section>

<section class="sheet folder">
  <div class="brand"><span class="dot"></span><span>Harborline<br>Chiropractic Center</span></div>
  <div class="band"></div>
  <div class="web">www.harborlineclinic-example.com</div>
</section>

<section class="sheet card-front">
  <div class="brand"><span class="dot"></span><span>Harborline Chiropractic Center</span></div>
  <div class="who">
    <strong>Dr. Tobias K. Feldmore</strong><br>
    Board Certified Chiropractor<br>
    4382 Elmhaven Ave, Suite 100<br>
    Frederick, MD 21745
  </div>
  <div class="band"></div>
</section>

<section class="sheet card-back">
  <div class="brand"><span class="dot"></span><span>Harborline Chiropractic Center</span></div>
  <div class="tag">Gentle Care, Lasting Results</div>
</section>

<section class="sheet envelope">
  <div class="brand"><span class="dot"></span><span>Harborline Chiropractic Center</span></div>
  <div class="band"></div>
  <div class="web">www.harborlineclinic-example.com</div>
</section>

<section class="sheet envelope-back">
  <svg viewBox="0 0 413 185" preserveAspectRatio="none" aria-hidden="true">
    <polyline points="0,0 206,92 413,0" fill="none" stroke="#dcdce2" stroke-width="1"/>
    <polyline points="0,185 150,84" fill="none" stroke="#e4e4ea" stroke-width="1"/>
    <polyline points="413,185 262,84" fill="none" stroke="#e4e4ea" stroke-width="1"/>
  </svg>
  <div class="web">www.harborlineclinic-example.com</div>
</section>

</body>
</html>
```